Velvet Lagoon Charm Boutique

Looking to refresh our old business cards. We are a girls/tween birthday party store and salon specializing in princess, glamour and spa parties. I would like to maintain the same colors (hot pink and turquoise). Would like the card to be feminine, fun and glitzy..

Target Market(s)

Parents of girls and girls aged 4-14

Industry/Entity Type

Store

Font styles to use
Script

Colors
e34197
85cae6

Requirements
Must have
• name phone and address
colors of hot pink and turquoise
appointment day and time field on one side
Nice to have
• creativity
Should not have
• picture of lipstick

```html
<!DOCTYPE html>
<html lang="en">
<head>
<meta charset="utf-8">
<title>Velvet Lagoon Charm Boutique – Business Cards</title>
<link rel="stylesheet" href="https://fonts.googleapis.com/css2?family=Great+Vibes&family=Quicksand:wght@400;500&display=swap">
<style>
  :root {
    --hot-pink: #e34197;
    --deep-pink: #c8177f;
    --blush: #f5bfdc;
    --blush-light: #fbe3f0;
    --turquoise: #85cae6;
    --white: #ffffff;
    --page: #efe9e4;
  }
  * { box-sizing: border-box; margin: 0; padding: 0; }
  html, body { width: 1200px; height: 1023px; overflow: hidden; }
  body {
    background: var(--page);
    position: relative;
    font-family: "Quicksand", sans-serif;
  }
  .card {
    position: absolute;
    width: 580px;
    height: 330px;
    border-radius: 22px;
    overflow: hidden;
    box-shadow: 0 8px 24px rgba(90, 40, 60, 0.18);
  }

  /* Front: contact side */
  .card-front {
    left: 60px;
    top: 90px;
    background: var(--blush);
  }
  .front-pattern {
    position: absolute;
    inset: 0;
    background: radial-gradient(ellipse at 50% 50%, var(--blush-light) 0%, var(--blush) 70%, #eea6cc 100%);
  }
  .front-panel {
    position: absolute;
    left: 70px; top: 48px;
    width: 440px; height: 234px;
    border: 3px solid var(--deep-pink);
    border-radius: 60px / 46px;
    background: repeating-linear-gradient(90deg, var(--white) 0 18px, #fdf1f7 18px 36px);
    display: flex;
    flex-direction: column;
    align-items: center;
    justify-content: center;
    text-align: center;
    gap: 6px;
  }
  .contact-name {
    font-family: "Great Vibes", cursive;
    font-size: 46px;
    color: var(--hot-pink);
    line-height: 1.1;
  }
  .contact-role,
  .contact-phone,
  .contact-address {
    color: var(--turquoise);
    font-size: 15px;
    letter-spacing: 0.5px;
  }
  .contact-role { text-transform: uppercase; font-size: 13px; letter-spacing: 1.5px; }

  /* Back: appointment side */
  .card-back {
    left: 560px;
    top: 570px;
    background: var(--hot-pink);
  }
  .back-pattern {
    position: absolute;
    inset: 0;
    background: radial-gradient(ellipse at 55% 40%, #ee62ad 0%, var(--hot-pink) 55%, var(--deep-pink) 100%);
  }
  .brand-name {
    position: absolute;
    top: 56px; left: 0; right: 0;
    text-align: center;
    color: var(--white);
    font-size: 30px;
    font-weight: 500;
    letter-spacing: 1px;
  }
  .tagline {
    position: absolute;
    top: 150px; left: 0; right: 0;
    text-align: center;
    font-family: "Great Vibes", cursive;
    font-size: 40px;
    color: var(--white);
  }
  .tagline .dot {
    display: inline-block;
    width: 10px; height: 10px;
    border-radius: 50%;
    background: var(--turquoise);
    margin: 0 12px;
    vertical-align: middle;
  }
  .appointment-strip {
    position: absolute;
    left: 26px; right: 26px; bottom: 28px;
    height: 58px;
    background: var(--white);
    border-radius: 0 0 22px 22px;
    display: flex;
    align-items: flex-end;
    gap: 28px;
    padding: 0 24px 14px;
  }
  .field {
    display: flex;
    align-items: flex-end;
    gap: 8px;
    font-size: 15px;
    color: var(--hot-pink);
  }
  .field-date { flex: 1.4; }
  .field-time { flex: 1; }
  .field-line {
    flex: 1;
    border-bottom: 1.5px solid var(--hot-pink);
    height: 1px;
    margin-bottom: 4px;
  }
</style>
</head>
<body>

  <section class="card card-front" aria-label="Contact side of business card">
    <div class="front-pattern" role="img" aria-label="Soft pink floral background pattern"></div>
    <div class="front-panel">
      <p class="contact-name">Dana Whitfield</p>
      <p class="contact-role">Owner</p>
      <p class="contact-phone">555 014 2297</p>
      <p class="contact-address">48 Harbor Lane, Maple Glen, New York 10999</p>
    </div>
  </section>

  <section class="card card-back" aria-label="Appointment side of business card">
    <div class="back-pattern" role="img" aria-label="Hot pink damask background pattern"></div>
    <p class="brand-name">Velvet Lagoon Charm Boutique</p>
    <p class="tagline">Spa<span class="dot"></span>Parties<span class="dot"></span>Boutique</p>
    <div class="appointment-strip">
      <div class="field field-date"><span>Date:</span><span class="field-line"></span></div>
      <div class="field field-time"><span>Time:</span><span class="field-line"></span></div>
    </div>
  </section>

</body>
</html>
```